Music Quizz Application

Hello,

I want a new design for my Blind test (music quizz) application on Velbix. You will find attached the images I want to replace. I need something with the same element (menu / song title) but with a different look!

Same, new icon, you have carte blanche to this one.

I am looking for something fresh…. I'm looking for something with a real artistic choice, contrast, colours, etc.

As a marketing screenshot, I want something classic, you'll find an example attached, feel free to innovate.

To sum-up :

- One new view for my App
- One new icon
- One marketing screenshot

screen resolution :
640×960
icon resolution :
1024x1024

Target Market(s)

15-30 years

Industry/Entity Type

Marketing

```html
<!DOCTYPE html>
<html lang="en">
<head>
<meta charset="utf-8">
<title>Velbix Music Quiz – Menu</title>
<link rel="stylesheet" href="https://fonts.googleapis.com/css2?family=Open+Sans:wght@400;600&family=Roboto:wght@700&display=swap">
<style>
  :root {
    --status-bg: #53595d;
    --status-text: #e6e8e9;
    --header-bg: #2c7590;
    --avatar-bg: #7b7c7d;
    --row-a: #338ba7;
    --row-b: #2e7f9a;
    --row-active: #3b97b3;
    --share-bg: #3186a2;
    --ink: #1c4a5c;
    --white: #ffffff;
    --panel-top-a: #8fd8d6;
    --panel-top-b: #5cbcc0;
    --panel-bar: #6ccdcc;
    --panel-foot: #2a6e86;
    --panel-text: #cde8ef;
    --social: #203f4c;
  }
  * { box-sizing: border-box; margin: 0; padding: 0; }
  html, body { width: 800px; height: 1200px; overflow: hidden; }
  body { position: relative; background: var(--row-b); font-family: "Open Sans", sans-serif; }

  .status-bar {
    position: absolute; left: 0; top: 0; width: 800px; height: 50px;
    background: var(--status-bg); color: var(--status-text);
    font-family: "Roboto", sans-serif; font-weight: 700; font-size: 28px;
  }
  .status-bar .signal { position: absolute; left: 10px; top: 14px; }
  .status-bar .carrier { position: absolute; left: 68px; top: 8px; letter-spacing: 0.5px; }
  .status-bar .clock { position: absolute; left: 0; width: 800px; text-align: center; top: 8px; }
  .status-bar .battery { position: absolute; right: 12px; top: 13px; }

  .drawer { position: absolute; left: 0; top: 50px; width: 708px; height: 1150px; }

  .profile { position: absolute; left: 0; top: 0; width: 708px; height: 221px; background: var(--header-bg); }
  .avatar {
    position: absolute; left: 0; top: 0; width: 224px; height: 221px; background: var(--avatar-bg);
    color: #eef0f1; font-size: 35px; line-height: 41px; padding: 66px 0 0 57px;
  }
  .profile .name { position: absolute; left: 262px; top: 38px; color: var(--white); font-size: 35px; }
  .profile .detail { position: absolute; left: 262px; color: var(--white); font-size: 26px; display: flex; align-items: center; gap: 14px; }
  .profile .email { top: 88px; }
  .profile .birthday { top: 142px; }

  .menu { position: absolute; left: 0; top: 221px; width: 708px; list-style: none; }
  .menu-item { position: relative; height: 110px; display: flex; align-items: center; color: var(--ink); font-size: 35px; }
  .menu-item:nth-child(odd) { background: var(--row-a); }
  .menu-item:nth-child(even) { background: var(--row-b); }
  .menu-item.active { background: var(--row-active); color: var(--white); }
  .menu-item .icon { position: absolute; left: 48px; top: 22px; width: 70px; height: 66px; }
  .menu-item .label { position: absolute; left: 169px; }
  .menu-item .go { position: absolute; left: 624px; top: 16px; }

  .share { position: absolute; left: 0; top: 881px; width: 708px; height: 269px; background: var(--share-bg); }
  .share .icon { position: absolute; left: 50px; top: 28px; }
  .share .title { position: absolute; left: 169px; top: 38px; color: var(--ink); font-size: 35px; }
  .social { position: absolute; top: 114px; width: 140px; text-align: center; }
  .social .mark { display: block; width: 90px; height: 90px; margin: 0 auto; background: var(--social); }
  .social .name { display: block; margin-top: 10px; color: var(--ink); font-size: 24px; }

  .content-panel { position: absolute; left: 708px; top: 50px; width: 92px; height: 1150px; overflow: hidden; }
  .content-panel .cover { position: absolute; left: 0; top: 0; width: 92px; height: 282px; background: linear-gradient(160deg, var(--panel-top-a), var(--panel-top-b)); }
  .content-panel .toolbar { position: absolute; left: 0; top: 0; width: 92px; height: 110px; background: var(--panel-bar); border-bottom: 3px solid #4aa8ad; }
  .content-panel .toolbar svg { position: absolute; left: 12px; top: 36px; }
  .songs { position: absolute; left: 0; top: 282px; width: 92px; list-style: none; }
  .songs li { height: 65px; padding: 12px 0 0 76px; font-weight: 600; font-size: 29px; color: var(--panel-text); white-space: nowrap; }
  .songs li:nth-child(odd) { background: var(--row-b); }
  .songs li:nth-child(even) { background: var(--row-a); }
  .content-panel .footer { position: absolute; left: 0; top: 1040px; width: 92px; height: 110px; background: var(--panel-foot); }
</style>
</head>
<body>
  <header class="status-bar">
    <svg class="signal" width="50" height="22" viewBox="0 0 50 22" fill="#e6e8e9">
      <rect x="0" y="16" width="6" height="6"/><rect x="10" y="12" width="6" height="10"/><rect x="20" y="8" width="6" height="14"/><rect x="30" y="4" width="6" height="18"/><rect x="40" y="0" width="6" height="22"/>
    </svg>
    <span class="carrier">VELNET</span>
    <span class="clock">2:34</span>
    <svg class="battery" width="52" height="26" viewBox="0 0 52 26">
      <rect x="1.5" y="1.5" width="44" height="23" rx="3" fill="none" stroke="#e6e8e9" stroke-width="3"/>
      <rect x="6" y="6" width="35" height="14" fill="#e6e8e9"/><rect x="47" y="8" width="4" height="10" fill="#e6e8e9"/>
    </svg>
  </header>

  <nav class="drawer">
    <section class="profile">
      <div class="avatar">Avatar<br>Image</div>
      <div class="name">Your name</div>
      <div class="detail email">
        <svg width="32" height="22" viewBox="0 0 32 22"><rect x="1.5" y="1.5" width="29" height="19" fill="none" stroke="#fff" stroke-width="2.5"/><path d="M2 3 L16 13 L30 3" fill="none" stroke="#fff" stroke-width="2.5"/></svg>
        <span>yourname@velmail.com</span>
      </div>
      <div class="detail birthday">
        <svg width="28" height="32" viewBox="0 0 28 32" fill="#fff"><rect x="1" y="9" width="26" height="7"/><rect x="3" y="17" width="22" height="14"/><rect x="12" y="9" width="4" height="22" fill="#2c7590"/><path d="M14 9 C8 0 2 4 8 9 Z M14 9 C20 0 26 4 20 9 Z"/></svg>
        <span>Dec 26 1988</span>
      </div>
    </section>

    <ul class="menu">
      <li class="menu-item">
        <svg class="icon" viewBox="0 0 70 66" fill="#1c4a5c"><path d="M35 4 L2 34 H10 V64 H60 V34 H68 Z"/><rect x="52" y="4" width="7" height="20"/><rect x="28" y="42" width="14" height="22" fill="#338ba7"/></svg>
        <span class="label">Home</span>
        <svg class="go" width="70" height="78" viewBox="0 0 70 78"><polygon points="35,4 66,21.5 66,56.5 35,74 4,56.5 4,21.5" fill="none" stroke="#1c4a5c" stroke-width="6"/><polygon points="26,24 26,54 50,39" fill="#1c4a5c"/></svg>
      </li>
      <li class="menu-item">
        <svg class="icon" viewBox="0 0 70 66" fill="#1c4a5c"><ellipse cx="35" cy="18" rx="14" ry="17"/><path d="M6 66 C6 46 18 40 35 40 C52 40 64 46 64 66 Z"/><path d="M32 40 H38 L40 60 L35 64 L30 60 Z" fill="#2e7f9a"/></svg>
        <span class="label">User Info</span>
        <svg class="go" width="70" height="78" viewBox="0 0 70 78"><polygon points="35,4 66,21.5 66,56.5 35,74 4,56.5 4,21.5" fill="none" stroke="#1c4a5c" stroke-width="6"/><polygon points="26,24 26,54 50,39" fill="#1c4a5c"/></svg>
      </li>
      <li class="menu-item active">
        <svg class="icon" viewBox="0 0 70 66" fill="#ffffff"><path d="M14 24 H56 C64 24 68 40 68 52 C68 60 60 62 54 54 L48 46 H22 L16 54 C10 62 2 60 2 52 C2 40 6 24 14 24 Z"/><path d="M36 22 C38 12 50 16 58 8" fill="none" stroke="#fff" stroke-width="2.5"/><g fill="#3b97b3"><rect x="12" y="33" width="14" height="4"/><rect x="17" y="28" width="4" height="14"/><circle cx="48" cy="30" r="2.5"/><circle cx="53" cy="35" r="2.5"/><circle cx="48" cy="40" r="2.5"/><circle cx="43" cy="35" r="2.5"/></g></svg>
        <span class="label">Play game</span>
        <svg class="go" width="70" height="78" viewBox="0 0 70 78"><polygon points="24,22 24,56 50,39" fill="#ffffff"/></svg>
      </li>
      <li class="menu-item">
        <svg class="icon" viewBox="0 0 70 66" fill="#1c4a5c"><rect x="23" y="2" width="24" height="24" rx="2"/><rect x="6" y="32" width="24" height="28" rx="2"/><rect x="34" y="32" width="24" height="28" rx="2"/><g fill="#338ba7" font-family="Open Sans, sans-serif" font-weight="600" font-size="18" text-anchor="middle"><text x="35" y="21">1</text><text x="18" y="53">2</text><text x="46" y="53">3</text></g></svg>
        <span class="label">Ranking</span>
        <svg class="go" width="70" height="78" viewBox="0 0 70 78"><polygon points="35,4 66,21.5 66,56.5 35,74 4,56.5 4,21.5" fill="none" stroke="#1c4a5c" stroke-width="6"/><polygon points="26,24 26,54 50,39" fill="#1c4a5c"/></svg>
      </li>
      <li class="menu-item">
        <svg class="icon" viewBox="0 0 70 66" fill="#1c4a5c"><circle cx="15" cy="16" r="8"/><circle cx="55" cy="16" r="8"/><circle cx="35" cy="10" r="9"/><path d="M2 52 V34 C2 26 28 26 28 34 V52 Z"/><path d="M42 52 V34 C42 26 68 26 68 34 V52 Z"/><path d="M20 62 V32 C20 22 50 22 50 32 V62 Z"/><circle cx="35" cy="38" r="8" fill="#2e7f9a"/><path d="M22 62 C22 50 48 50 48 62 Z" fill="#2e7f9a"/></svg>
        <span class="label">Community</span>
        <svg class="go" width="70" height="78" viewBox="0 0 70 78"><polygon points="35,4 66,21.5 66,56.5 35,74 4,56.5 4,21.5" fill="none" stroke="#1c4a5c" stroke-width="6"/><polygon points="26,24 26,54 50,39" fill="#1c4a5c"/></svg>
      </li>
      <li class="menu-item">
        <svg class="icon" viewBox="0 0 70 66"><circle cx="33" cy="33" r="33" fill="#1c4a5c"/><circle cx="36" cy="18" r="5" fill="#338ba7"/><path d="M28 28 H40 L35 50 H40 L39 54 H26 L31 32 H27 Z" fill="#338ba7"/></svg>
        <span class="label">About</span>
        <svg class="go" width="70" height="78" viewBox="0 0 70 78"><polygon points="35,4 66,21.5 66,56.5 35,74 4,56.5 4,21.5" fill="none" stroke="#1c4a5c" stroke-width="6"/><polygon points="26,24 26,54 50,39" fill="#1c4a5c"/></svg>
      </li>
    </ul>

    <section class="share">
      <svg class="icon" width="66" height="66" viewBox="0 0 66 66"><circle cx="33" cy="33" r="31" fill="#1c4a5c"/><path d="M12 20 C20 14 28 18 26 28 C24 36 14 34 12 42 Z M36 8 C44 14 40 20 46 24 C54 28 52 40 44 42 C36 44 40 54 34 58 C30 48 28 40 34 34 C40 28 30 20 36 8 Z" fill="#3186a2"/></svg>
      <div class="title">Share with your friend</div>
      <div class="social" style="left:140px"><span class="mark"></span><span class="name">Friendo</span></div>
      <div class="social" style="left:278px"><span class="mark"></span><span class="name">Buzzly</span></div>
      <div class="social" style="left:416px"><span class="mark"></span><span class="name">Circla</span></div>
    </section>
  </nav>

  <main class="content-panel">
    <div class="cover" role="img" aria-label="Blurred album artwork for the current song"></div>
    <div class="toolbar">
      <svg width="40" height="34" viewBox="0 0 40 34" fill="#1c4a5c"><rect x="2" y="2" width="6" height="6"/><rect x="12" y="2" width="26" height="6"/><rect x="2" y="14" width="6" height="6"/><rect x="12" y="14" width="26" height="6"/><rect x="2" y="26" width="6" height="6"/><rect x="12" y="26" width="26" height="6"/></svg>
    </div>
    <ul class="songs">
      <li>Hits</li><li>Pop</li><li>Punk</li><li>New</li><li>Rock</li><li>House</li>
      <li>90s</li><li>Indie</li><li>Rap</li><li>Disco</li><li>Alt</li><li>Chill</li>
    </ul>
    <div class="footer"></div>
  </main>
</body>
</html>
```